Beauty Clinic Treatment Menu (Lumen Nails & Beauty)

Needing a treatment menu designed for a beauty clinic in Whitianga, New Zealand. Like the colours grey, pink, white.
Elegant, Modern and feminine

Lumen Nails & Beauty
Karen Pell
Room3, 48 Tainui Street
Whitianga
0273816240
Karen.lumen@mailbox.test
lumenbeauty.co.nz

Target Market(s)

Females

Industry/Entity Type

Beauty Salon

Font styles to use
Serif

Colors

Requirements
Must have
• Chatterly and Snapgrid logo

```html
<!DOCTYPE html>
<html lang="en">
<head>
<meta charset="utf-8">
<title>Lumen Nails &amp; Beauty – Treatment Menu</title>
<link rel="stylesheet" href="https://fonts.googleapis.com/css2?family=Kaushan+Script&family=Montserrat:wght@400&display=swap">
<style>
  :root {
    --backdrop: #e6e4e1;
    --paper: #f7f7f7;
    --wash-light: #f8e3ec;
    --wash-mid: #f5c6da;
    --wash-deep: #f3adcc;
    --rose-gold: #b08a70;
    --menu-white: #ffffff;
  }
  * { margin: 0; padding: 0; box-sizing: border-box; }
  html, body {
    width: 816px;
    height: 1200px;
    overflow: hidden;
    background: var(--backdrop);
  }
  .cover {
    position: absolute;
    left: 84px;
    top: 0;
    width: 648px;
    height: 1200px;
    background: var(--paper);
    overflow: hidden;
  }
  .watercolour-wash {
    position: absolute;
    inset: 0;
    width: 100%;
    height: 100%;
  }
  .brand {
    position: absolute;
    left: 160px;
    top: 396px;
    width: 312px;
    height: 312px;
    display: flex;
    flex-direction: column;
    align-items: center;
    justify-content: center;
  }
  .brand-ring {
    position: absolute;
    inset: 0;
    border: 2px solid var(--rose-gold);
    border-radius: 50%;
  }
  .brand-name,
  .brand-tagline {
    position: relative;
    font-family: "Montserrat", sans-serif;
    font-weight: 400;
    color: var(--rose-gold);
  }
  .brand-name {
    font-size: 62px;
    letter-spacing: 2px;
    line-height: 1;
  }
  .brand-tagline {
    margin-top: 26px;
    font-size: 16px;
    letter-spacing: 0.5px;
  }
  .menu-title {
    position: absolute;
    left: 2px;
    top: 860px;
    font-family: "Kaushan Script", cursive;
    font-size: 300px;
    line-height: 1;
    color: var(--menu-white);
    white-space: nowrap;
    letter-spacing: -6px;
  }
</style>
</head>
<body>
  <main class="cover">
    <svg class="watercolour-wash" viewBox="0 0 648 1200" preserveAspectRatio="none" role="img" aria-label="Soft pink watercolour wash spreading from the upper right down across the lower cover">
      <defs>
        <linearGradient id="washFill" x1="0" y1="0" x2="0" y2="1">
          <stop offset="0" stop-color="var(--wash-light)"/>
          <stop offset="0.45" stop-color="var(--wash-mid)"/>
          <stop offset="1" stop-color="var(--wash-deep)"/>
        </linearGradient>
        <filter id="washSoften" x="-10%" y="-10%" width="120%" height="120%">
          <feGaussianBlur stdDeviation="10"/>
        </filter>
      </defs>
      <path filter="url(#washSoften)" fill="url(#washFill)"
        d="M660 220 C600 250 560 300 540 360 C500 380 470 420 440 470
           C400 500 340 520 300 560 C250 600 220 680 140 720
           C80 750 20 780 -20 820 L-20 1220 L660 1220 Z"/>
      <path filter="url(#washSoften)" fill="var(--wash-deep)" opacity="0.55"
        d="M660 640 C600 700 520 760 430 800 C330 850 200 880 -20 930 L-20 1220 L660 1220 Z"/>
    </svg>

    <div class="brand">
      <span class="brand-ring"></span>
      <span class="brand-name">Lumen</span>
      <span class="brand-tagline">Nails &amp; Beauty</span>
    </div>

    <h1 class="menu-title">Menu</h1>
  </main>
</body>
</html>
```